The Larkwell Stillhouse - Gin Bottle Label

Hi Designers,

We are currently looking for some fresh ideas regarding a label for our gin bottle. We are relatively small and with an emphasis on a quality tipple
made from the very finest and responsibly sourced botanicals. Our operation concentrates on small batch/hand crafted in its purest sense and we would like to reflect this in our brand.
We are looking for a label to read The Larkwell Stillhouse and have feminine accents with a primary background colour similar to Marlowe green/blue. Things like Sakura branches with blossom, floral, pretty scrolling perhaps around either full or partial boarder. Gold foil might be used to accent the black border/highlight the word "Boutique" and perhaps any floral pattern.
There could reconsideration given to include two boxes "Batch No" and "Bottle No" which would remain empty and filled out by hand during bottling.
Our gin will be 45%ABV
Some floral designs might look good as though they were watercolours in appearance perhaps.
Our bottles are clear medicine style of which I shall attatch a pic.
We are pretty excited about this and would invite anyone with flair and great ideas to have fun with this design.

With kind regards,

Ned

Target Market(s)

People who adore bespoke Gin and would be predominately female.

Colors
86cfc6

Requirements
Must have
• We love the Marlowe green tones and this well may be our label colour with your design.
• The Larkwell Stillhouse - Gin - 45ABV
Nice to have
• Batch No & Bottle No boxes

```html
<!DOCTYPE html>
<html lang="en">
<head>
<meta charset="utf-8">
<title>The Larkwell Stillhouse – Gin Label</title>
<link href="https://fonts.googleapis.com/css2?family=Marcellus&family=Oswald:wght@300;600&display=swap" rel="stylesheet">
<style>
  :root {
    --page: #f3f3f3;
    --label-teal: #a8dcd9;
    --frame-white: #eef8f7;
    --gold: #e3cf3c;
    --ink-grey: #6b6b6b;
    --ink-dark: #5f5f5f;
    --blossom-pink: #f2b9cb;
  }
  * { margin: 0; padding: 0; box-sizing: border-box; }
  html, body {
    width: 1200px;
    height: 1106px;
    overflow: hidden;
    background: var(--page);
  }
  .label {
    position: absolute;
    left: 129px;
    top: 53px;
    width: 942px;
    height: 1000px;
    background: var(--label-teal);
    overflow: hidden;
  }
  .frame-outer {
    position: absolute;
    left: 119px;
    top: 114px;
    width: 696px;
    height: 777px;
    border: 30px solid var(--frame-white);
  }
  .frame-gold {
    position: absolute;
    left: 183px;
    top: 185px;
    width: 573px;
    height: 643px;
    border: 5px solid var(--gold);
  }
  .blossom {
    position: absolute;
    border-radius: 50%;
    background: radial-gradient(ellipse at center, var(--blossom-pink) 0%, rgba(224,122,155,0.5) 45%, rgba(106,74,63,0.15) 70%, rgba(168,220,217,0) 100%);
  }
  .blossom--top-right { left: 640px; top: -40px; width: 360px; height: 400px; }
  .blossom--left { left: -40px; top: 331px; width: 260px; height: 510px; }
  .blossom--bottom { left: 233px; top: 815px; width: 661px; height: 170px; }
  .content {
    position: absolute;
    left: 188px;
    top: 190px;
    width: 563px;
    height: 633px;
    text-align: center;
    color: var(--ink-grey);
  }
  .brand-name {
    position: absolute;
    top: 70px;
    width: 100%;
    font-family: "Marcellus", serif;
    font-weight: 400;
    font-size: 56px;
    line-height: 1.12;
    color: var(--ink-grey);
  }
  .product-name {
    position: absolute;
    top: 255px;
    width: 100%;
    font-family: "Oswald", sans-serif;
    font-weight: 600;
    font-size: 140px;
    line-height: 1;
    letter-spacing: 8px;
    color: var(--ink-dark);
  }
  .tagline {
    position: absolute;
    top: 452px;
    width: 100%;
    font-family: "Oswald", sans-serif;
    font-weight: 300;
    font-size: 26px;
    letter-spacing: 1px;
    color: var(--ink-dark);
  }
  .strength {
    position: absolute;
    top: 548px;
    width: 100%;
    font-family: "Oswald", sans-serif;
    font-weight: 300;
    font-size: 38px;
    letter-spacing: 3px;
    color: var(--ink-dark);
  }
</style>
</head>
<body>
  <main class="label">
    <div class="frame-outer"></div>
    <div class="frame-gold"></div>

    <div class="blossom blossom--top-right" role="img" aria-label="Watercolour sakura branch with pink blossom reaching across the top right corner"></div>
    <div class="blossom blossom--left" role="img" aria-label="Sakura branch with pink blossom trailing down the left edge"></div>
    <div class="blossom blossom--bottom" role="img" aria-label="Scattered pink sakura blossom along the lower frame"></div>

    <section class="content">
      <h1 class="brand-name">The Larkwell<br>Stillhouse</h1>
      <p class="product-name">GIN</p>
      <p class="tagline">THE FINEST SMALL BATCH HAND CRAFTED</p>
      <p class="strength">45%ABV</p>
    </section>
  </main>
</body>
</html>
```